Veltorix needs web site design

We need a web site design for our product called 'Veltorix'. We develop an asset management system that can manage all kind of assets. Currently we have a logo theme and would like to use similar color scheme; the content concept is pretty much in http://tbaldwyn.example but the product was called "Keystone Lab" at the time and is now called "Veltorix". Velto means Unified Ledger Tracking Operations Network Agency.
Please use generic image for asset (not just bridges) e.g buildings, trucks, powerlines. train, bus, lightrail etc..
Please emphazise on the data management and security, and distributed networking.

the new website address is https://www.veltorix.example/

name on business card

Thomas Baldwyn 555-014-7723
Principal Architect / Software Engineer

Dana Baldwyn 555-018-2946
Software Engineer

Coding

Coded - Design and coding required

Number of Pages Required

1 page

```html
<!DOCTYPE html>
<html lang="en">
<head>
<meta charset="utf-8">
<title>Veltorix Asset Management</title>
<link rel="stylesheet" href="https://fonts.googleapis.com/css2?family=Play:wght@400;700&family=Poppins:wght@400;500;600&display=swap">
<style>
:root{
  --navy:#0b1c7c;
  --gold:#c9a240;
  --gold-dark:#a9832e;
  --ink:#222;
  --muted:#444;
  --light:#f4f4f4;
  --footer:#262626;
  --white:#fff;
}
*{box-sizing:border-box;margin:0;padding:0}
html,body{width:1200px;height:2857px;overflow:hidden}
body{font-family:"Poppins",sans-serif;color:var(--ink);background:var(--white);position:relative}
.abs{position:absolute}
h2,.display{font-family:"Play",sans-serif;font-weight:400}

/* header */
.site-header{position:absolute;left:0;top:0;width:1200px;height:118px;background:var(--white)}
.brand{position:absolute;left:120px;top:36px;display:flex;align-items:center;gap:12px}
.brand-mark{width:40px;height:40px;background:var(--navy)}
.brand-name{font-family:"Play",sans-serif;font-size:36px;color:var(--navy);font-weight:700}
.top-contacts{position:absolute;right:118px;top:22px;display:flex;gap:34px;font-size:13px;color:var(--ink)}
.top-contacts span{display:flex;align-items:center;gap:8px}
.dot-icon{width:20px;height:20px;border-radius:50%;background:var(--gold);display:inline-block}
.main-nav{position:absolute;right:120px;top:64px;display:flex;align-items:center;gap:26px;font-size:14px}
.main-nav a{color:var(--ink);text-decoration:none}
.main-nav .active{border-bottom:2px solid var(--navy);padding-bottom:3px}
.btn-login{background:var(--navy);color:#fff!important;border-radius:14px;padding:4px 28px}

/* hero */
.hero{position:absolute;left:0;top:118px;width:1200px;height:572px;
  background:linear-gradient(100deg,#1c1a18 0%,#3a3530 40%,#6a5a48 70%,#3b3128 100%)}
.hero-shot{position:absolute;left:520px;top:30px;width:420px;height:300px;border-radius:8px;
  background:linear-gradient(160deg,#bcd6f0,#2f6fb8)}
.hero-title{position:absolute;left:200px;top:262px;width:350px;text-align:center;color:#fff;font-family:"Play",sans-serif;font-size:28px;line-height:34px}
.btn-gold{display:inline-block;background:var(--gold);color:#fff;border-radius:14px;font-size:13px;text-align:center}
.hero .btn-gold{position:absolute;left:320px;top:344px;width:118px;height:28px;line-height:28px}
.arrow{position:absolute;top:278px;width:32px;height:32px;border-radius:50%}
.arrow.prev{left:42px;background:#555}
.arrow.next{right:42px;background:var(--gold)}
.hero-dots{position:absolute;left:584px;top:706px;display:flex;gap:4px}
.hero-dots i{width:5px;height:5px;border-radius:50%;background:#333}
.hero-dots i:first-child{background:var(--gold)}

/* services */
.services{position:absolute;left:0;top:690px;width:1200px;height:460px;background:var(--light)}
.section-title{position:absolute;left:0;width:1200px;text-align:center;font-size:30px}
.section-sub{position:absolute;left:0;width:1200px;text-align:center;font-size:12px;font-weight:500}
.service{position:absolute;top:138px;width:228px;height:238px;text-align:center;padding-top:26px;border-radius:12px}
.service.is-active{background:var(--navy);color:#fff}
.service-icon{width:64px;height:64px;margin:0 auto 24px}
.service h3{font-family:"Play",sans-serif;font-weight:400;font-size:17px;line-height:21px;margin-bottom:12px}
.service p{font-size:12px;line-height:16px;padding:0 30px}

/* portfolio */
.portfolio{position:absolute;left:0;top:1150px;width:1200px;height:645px;
  background:linear-gradient(135deg,var(--gold-dark),#c9a54e 45%,#b08a35)}
.portfolio .section-title{color:#fff;top:48px}
.filters{position:absolute;top:104px;left:0;width:1200px;display:flex;justify-content:center;color:#fff;font-size:16px}
.filters span{padding:0 18px;border-left:1px solid rgba(255,255,255,.7)}
.filters span:first-child{border-left:none}
.tile{position:absolute;width:303px;height:171px;background:#fff}
.tile .art{position:absolute;left:60px;top:25px;width:183px;height:121px;border-radius:6px}
.tile.feature{background:#333;color:#fff}
.tile.feature .label{position:absolute;left:0;top:72px;width:303px;text-align:center;font-size:17px}
.portfolio .btn-gold{position:absolute;left:546px;top:578px;width:122px;height:28px;line-height:28px;background:#fff;color:var(--gold)}

/* download */
.download .section-title{top:1860px}
.download .section-sub{top:1897px}
.download-copy{position:absolute;left:120px;top:1970px;width:490px;font-size:13px;line-height:18px}
.download-copy p{margin-bottom:18px}
.btn-row{position:absolute;left:120px;top:2134px;display:flex;gap:28px;align-items:center}
.btn-row .btn-gold{width:168px;height:28px;line-height:28px}
.btn-navy{display:flex;align-items:center;gap:10px;background:var(--navy);color:#fff;border-radius:14px 0 0 14px;height:28px;padding-left:24px;width:130px;font-size:13px}
.download-art{position:absolute;left:705px;top:1935px;width:305px;height:285px;border-radius:10px;
  background:radial-gradient(circle at 70% 65%,#f2c4b4,#e9e9e9 60%,#fff)}

/* newsletter */
.newsletter-title{position:absolute;top:2270px;left:0;width:1200px;text-align:center;font-family:"Play",sans-serif;font-size:26px}
.newsletter-sub{position:absolute;top:2308px;left:0;width:1200px;text-align:center;font-size:13px}
.newsletter-form{position:absolute;left:310px;top:2346px;width:558px;height:38px;display:flex;border:1px solid #ddd;border-radius:19px;overflow:hidden}
.newsletter-form .field{flex:1;padding-left:22px;line-height:36px;font-size:13px;color:#999}
.newsletter-form .submit{width:126px;background:var(--gold);color:#fff;font-weight:600;text-align:center;line-height:36px;font-size:14px;border-radius:19px}

/* footer */
.site-footer{position:absolute;left:0;top:2460px;width:1200px;height:345px;background:var(--footer);color:#fff}
.site-footer .brand{left:120px;top:72px}
.site-footer .brand-mark{background:#fff}
.site-footer .brand-name{color:#fff}
.footer-about{position:absolute;left:120px;top:146px;width:270px;font-size:12px;line-height:18px;font-weight:600}
.footer-about .more{display:block;margin-top:8px}
.footer-col{position:absolute;top:90px;font-size:12px;font-weight:500}
.footer-col h4{font-family:"Play",sans-serif;font-weight:700;font-size:14px;border-bottom:2px solid var(--gold);display:inline-block;padding-bottom:4px;margin-bottom:46px}
.footer-col li{list-style:none;line-height:20.5px}
.quick-links li::before{content:"➤ ";font-size:9px}
.contact-list li{line-height:28px}
.qc-input{position:absolute;background:#3a3a3a;border-radius:8px;font-size:11px;padding:4px 12px;color:#ddd}
.qc-send{position:absolute;left:964px;top:2700px;width:116px;height:24px;line-height:24px;font-size:13px;background:var(--gold);color:var(--ink);border-radius:12px;text-align:center}
.copyright-bar{position:absolute;left:0;top:2805px;width:1200px;height:52px;background:var(--gold)}
.copyright-bar p{position:absolute;left:120px;top:16px;font-size:15px;font-weight:600}
.social{position:absolute;right:120px;top:12px;display:flex;gap:12px}
.social i{width:26px;height:26px;border-radius:50%;background:#222}
</style>
</head>
<body>

<header class="site-header">
  <div class="brand"><span class="brand-mark"></span><span class="brand-name">Veltorix</span></div>
  <div class="top-contacts">
    <span><i class="dot-icon"></i>info@veltorix.example</span>
    <span><i class="dot-icon"></i>0800 55 19 40</span>
  </div>
  <nav class="main-nav">
    <a class="active">Home</a><a>About</a><a>Services</a><a>Portfolio</a><a>Download</a><a>Contact</a><a class="btn-login">Login</a>
  </nav>
</header>

<section class="hero">
  <div class="hero-shot" role="img" aria-label="Photo of hands typing on a laptop showing the product screen"></div>
  <div class="hero-title">Software Development<br>Services</div>
  <span class="btn-gold">Read More</span>
  <svg class="arrow prev" viewBox="0 0 32 32"><circle cx="16" cy="16" r="16" fill="#555"/><path d="M18 10l-6 6 6 6" stroke="#fff" stroke-width="2.5" fill="none"/></svg>
  <svg class="arrow next" viewBox="0 0 32 32"><circle cx="16" cy="16" r="16" fill="#c9a240"/><path d="M14 10l6 6-6 6" stroke="#fff" stroke-width="2.5" fill="none"/></svg>
</section>
<div class="hero-dots"><i></i><i></i><i></i><i></i></div>

<section class="services">
  <h2 class="section-title" style="top:48px">Services</h2>
  <p class="section-sub" style="top:90px">Lorem Ipsum is simply the dummy of the printing</p>
  <div class="service" style="left:122px">
    <div class="service-icon" role="img" aria-label="Globe icon" style="background:radial-gradient(circle,#e2b550,#c9922c);border-radius:50%"></div>
    <h3>Web and Network Based<br>Information System</h3>
    <p>Lorem Ipsum is simply the dummy of the printing and industry...</p>
  </div>
  <div class="service is-active" style="left:366px">
    <div class="service-icon" role="img" aria-label="Team gear icon" style="background:radial-gradient(circle,#f0c050 30%,transparent 32%),radial-gradient(circle,transparent 45%,#e8b23e 47%,#e8b23e 62%,transparent 64%)"></div>
    <h3>Software Project<br>Management</h3>
    <p>Lorem Ipsum is simply the dummy of the printing and industry...</p>
  </div>
  <div class="service" style="left:608px">
    <div class="service-icon" role="img" aria-label="Monitor with gear icon" style="background:linear-gradient(#e3a94a,#d08a2a);border-radius:6px;height:48px;margin-bottom:40px"></div>
    <h3>Software<br>Development</h3>
    <p>Lorem Ipsum is simply the dummy of the printing and industry...</p>
  </div>
  <div class="service" style="left:850px">
    <div class="service-icon" role="img" aria-label="Consultant at desk icon" style="background:linear-gradient(#efbf5a,#d59a34);border-radius:8px"></div>
    <h3>Computing<br>Consultant</h3>
    <p>Lorem Ipsum is simply the dummy of the printing and industry...</p>
  </div>
</section>

<section class="portfolio">
  <h2 class="section-title">Portfolio</h2>
  <div class="filters"><span>All</span><span>Network Based Information System</span><span>Software Project Management</span><span>Software Development</span></div>
  <div class="tile feature" style="left:118px;top:174px"><span class="label">Keystone Lab &#8853;</span></div>
  <div class="tile" style="left:448px;top:174px"><div class="art" role="img" aria-label="Illustration of coloured task bars and a stopwatch" style="background:linear-gradient(90deg,#3aa0e0,#f0a020,#e03a3a)"></div></div>
  <div class="tile" style="left:777px;top:174px"><div class="art" role="img" aria-label="Illustration of a wrench and repair symbol" style="background:linear-gradient(#2a2a2a,#666)"></div></div>
  <div class="tile" style="left:118px;top:374px"><div class="art" role="img" aria-label="Illustration of a network of connected nodes" style="background:radial-gradient(circle,#e03a5a,#4a7ad0 60%,#fff)"></div></div>
  <div class="tile" style="left:448px;top:374px"><div class="art" role="img" aria-label="Illustration of a database linked to devices" style="background:radial-gradient(circle,#4a6ad0,#f0b040 60%,#fff)"></div></div>
  <div class="tile" style="left:777px;top:374px"><div class="art" role="img" aria-label="Illustration of a laptop with application windows" style="background:linear-gradient(120deg,#3a8a4a,#d04ab0)"></div></div>
  <span class="btn-gold">Read More</span>
</section>

<section class="download">
  <h2 class="section-title">Download</h2>
  <p class="section-sub">Lorem Ipsum is simply the dummy of the printing</p>
  <div class="download-copy">
    <p>The following demonstration software is available:</p>
    <p>Keystone Lab workstation demonstration software. A full copy of the Keystone Lab workstation software that connects to a demonstration<br><br>server.<br>Qlib Extensions utilities. A useful set of license free extensions to the Qlib system.</p>
  </div>
  <div class="btn-row">
    <span class="btn-gold">Read More</span>
    <span class="btn-navy">Download
      <svg width="44" height="34" viewBox="0 0 44 34"><path d="M10 28a8 8 0 0 1 0-16 11 11 0 0 1 21-3 9 9 0 0 1 3 19z" fill="#fff" stroke="#0b1c7c" stroke-width="2"/><path d="M22 12v12m-5-5l5 5 5-5" stroke="#0b1c7c" stroke-width="2.2" fill="none"/></svg>
    </span>
  </div>
  <div class="download-art" role="img" aria-label="Software box and disc illustration"></div>
</section>

<h2 class="newsletter-title">Subscribe To Our Newsletter</h2>
<p class="newsletter-sub">To Receive The latest News And Update</p>
<div class="newsletter-form"><span class="field">Your E-Mail</span><span class="submit">SUBMIT</span></div>

<footer class="site-footer">
  <div class="brand"><span class="brand-mark"></span><span class="brand-name">Veltorix</span></div>
  <p class="footer-about">Lorem Ipsum is simply dummy text of the printing and typesetting indu stry. Lorem text of the printing and typeset Ipsum.industries.<span class="more">Read More.</span></p>
  <div class="footer-col quick-links" style="left:436px"><h4>Quick Links</h4>
    <ul><li>Home</li><li>About</li><li>Services</li><li>Portfolio</li><li>Download</li><li>Contact</li></ul></div>
  <div class="footer-col contact-list" style="left:620px"><h4 style="margin-bottom:34px">Contact us</h4>
    <ul><li>Halvorsen &amp; Associates</li><li>Eastbrook, WA</li><li>98123-4401</li><li>555-014-7723</li><li>Support@tbaldwyn.example</li></ul></div>
  <div class="footer-col" style="left:852px"><h4>Quick Contact</h4></div>
  <span class="qc-input" style="left:852px;top:156px;width:112px">Name</span>
  <span class="qc-input" style="left:970px;top:156px;width:110px">Phone</span>
  <span class="qc-input" style="left:852px;top:180px;width:228px;height:52px">Message</span>
</footer>
<span class="qc-send">Send</span>

<div class="copyright-bar">
  <p>Copyright © 2018 Veltorix.&nbsp; All Rights Reserved.</p>
  <div class="social"><i></i><i></i><i></i><i></i><i></i></div>
</div>

</body>
</html>
```